Website redesign

Looking to redesign our existing website. (quill7meadows.com.au)
New design needs to be bright, fun and have an easy flowing.
The website needs to be design with call to action.

Some examples of other websites:
fernquaylo.com
tovanmilk.com.au

We are happy with the content of our existing website.

Target Market(s)

other businesses

Industry/Entity Type

Business Service

Number of Pages Required

5+ page

Requirements
Must have
• Theme redesign
Cool animation similar to fernquaylo.com

```html
<!DOCTYPE html>
<html lang="en">
<head>
<meta charset="utf-8">
<title>Quill 7 Meadows — Virtual Assistants</title>
<link rel="stylesheet" href="https://fonts.googleapis.com/css2?family=Montserrat:wght@300;400;500;600&display=swap">
<style>
:root{
  --blue:#10ade2;
  --blue-dark:#0c97c9;
  --mist:#cdd0df;
  --mist-light:#dfe1ea;
  --ink:#222;
  --text:#444;
  --white:#fff;
  --bar:#333;
}
*{box-sizing:border-box;margin:0;padding:0}
html,body{width:1200px;height:2173px;overflow:hidden}
body{position:relative;font-family:'Montserrat',sans-serif;color:var(--ink);background:var(--white)}
.abs{position:absolute}

/* header */
.site-header{position:absolute;left:0;top:0;width:1200px;height:50px;border-bottom:2px solid #e4e4e4;background:var(--white)}
.brand{position:absolute;text-align:center;color:var(--ink);font-weight:600}
.brand .brand-mark{display:block;font-size:20px;line-height:22px}
.brand .brand-name{display:block;font-size:10px;line-height:12px}
.main-nav{position:absolute;top:18px;left:408px;display:flex;gap:0}
.main-nav a{font-size:10px;color:var(--ink);text-decoration:none;line-height:12px;margin-right:26px}
.call-pill{position:absolute;left:781px;top:14px;width:194px;height:21px;border-radius:11px;background:var(--mist);overflow:hidden}
.call-pill .call-label{position:absolute;left:0;top:0;width:100px;height:21px;border-radius:11px;background:var(--blue);color:var(--white);font-size:12px;line-height:21px;padding-left:12px}
.call-pill .call-label svg{position:absolute;right:4px;top:2px}
.call-pill .call-number{position:absolute;left:114px;top:0;font-size:12px;line-height:21px;color:var(--blue);font-weight:500}

/* hero */
.hero-title{left:225px;top:203px;font-size:31px;font-weight:400;color:var(--blue);letter-spacing:-.5px}
.hero-sub{left:226px;top:251px;font-size:21px;font-weight:400;color:var(--ink);letter-spacing:-.3px}
.btn-quote{left:225px;top:295px;width:156px;height:31px;border-radius:16px;background:var(--blue);color:var(--white);font-size:15px;line-height:31px;text-align:center;text-decoration:none}
.hero-art{left:565px;top:100px;width:605px;height:355px;border-radius:50% 50% 46% 46%;background:radial-gradient(ellipse at center,#eef0f7 0%,#dcdff0 55%,rgba(220,223,240,0) 72%)}

/* intro band */
.intro{left:0;top:485px;width:1200px;height:276px;background:var(--mist)}
.intro-title{left:225px;top:512px;font-size:21px;font-weight:400;color:var(--white);letter-spacing:-.3px}
.intro-title .hl{color:var(--blue)}
.intro-copy{left:226px;top:545px;width:345px;font-size:11px;line-height:17px;color:var(--white);font-weight:300}
.intro-video{left:632px;top:553px;width:342px;height:176px;background:linear-gradient(90deg,#5a8db8 0%,#2f5f8e 55%,#1f3d5f 100%)}

/* process */
.process{left:0;top:761px;width:1200px;height:357px;background:var(--blue)}
.process-title{left:0;top:788px;width:1200px;text-align:center;font-size:21px;color:var(--white);font-weight:400}
.process-line{left:0;top:869px;width:1200px;height:1px;background:rgba(255,255,255,.8)}
.step{position:absolute;border-radius:50%;background:var(--mist);border:2px solid var(--white);color:#888;text-align:center;display:flex;flex-direction:column;justify-content:center;font-weight:300;box-shadow:0 2px 4px rgba(0,0,0,.15)}
.step.sm{width:48px;height:48px;font-size:9px;line-height:13px;opacity:.85}
.step.md{width:56px;height:56px;font-size:12px;line-height:18px}
.step.lg{width:62px;height:62px;font-size:15px;line-height:21px;color:#777}
.card{position:absolute;background:var(--mist);overflow:hidden;box-shadow:0 2px 5px rgba(0,0,0,.15)}
.card h3{font-weight:500;color:#666}
.card p{color:#999;font-weight:300}
.card.far{opacity:.9;padding:4px 5px}
.card.far h3{font-size:8px;line-height:11px}
.card.far p{font-size:5px;line-height:9px}
.card.near{padding:5px 7px}
.card.near h3{font-size:9px;line-height:11px;color:#888}
.card.near p{font-size:5.5px;line-height:9px}
.card.main{padding:10px 12px;z-index:2}
.card.main h3{font-size:12px;line-height:14px;color:var(--ink);margin-bottom:4px}
.card.main p{font-size:9.5px;line-height:23px;color:#333;padding-left:2px}

/* services */
.services-title{left:0;top:1145px;width:1200px;text-align:center;font-size:21px;color:var(--ink);font-weight:400}
.services-lead{left:0;top:1174px;width:1200px;text-align:center;font-size:14.5px;color:var(--ink)}
.services-ask{left:0;top:1198px;width:1200px;text-align:center;font-size:14.5px;color:var(--blue)}
.service{position:absolute;top:1243px;width:240px;text-align:center}
.service-ring{margin:0 auto;width:134px;height:134px;border-radius:50%;border:2px solid var(--blue);padding:7px}
.service-art{width:116px;height:116px;border-radius:50%;background:radial-gradient(circle,#3fc0ee 0%,var(--blue) 70%)}
.service p{margin-top:8px;font-size:10.5px;line-height:24px;color:var(--ink)}

/* quote */
.quote{left:0;top:1505px;width:1200px;height:438px;background:var(--blue)}
.quote-title{left:224px;top:1532px;font-size:21px;color:var(--white);font-weight:400}
.quote-lead{left:225px;top:1566px;width:300px;font-size:12px;line-height:19px;color:var(--white)}
.perks{left:225px;top:1626px;list-style:none}
.perks li{position:relative;height:31.4px;padding-left:29px;font-size:12.5px;line-height:22px;color:var(--white)}
.perks li svg{position:absolute;left:0;top:0}
.quote-form{left:599px;top:1537px;width:376px;height:374px;background:var(--white)}
.field{position:absolute;left:32px;width:312px;height:21px;border-radius:11px;background:var(--mist);border:1px solid #4f8fe0;overflow:hidden}
.field .field-label{position:absolute;left:0;top:0;width:134px;height:19px;border-radius:10px;background:var(--blue);color:var(--white);font-size:12px;line-height:19px;padding-left:5px}
.field .field-label svg{position:absolute;right:7px;top:1px}
.field-area{position:absolute;left:32px;top:218px;width:312px;height:100px;border-radius:10px;background:var(--mist);border:1px solid #4f8fe0;overflow:hidden}
.field-area .field-label{height:38px;background:var(--blue);color:var(--white);font-size:12px;line-height:15px;padding:3px 6px;position:relative}
.field-area .field-label svg{position:absolute;right:6px;top:6px}
.subscribe{position:absolute;left:32px;top:339px;font-size:12px;color:var(--blue);line-height:14px;padding-left:19px}
.subscribe::before{content:"";position:absolute;left:0;top:1px;width:10px;height:10px;border:1px solid var(--blue);border-radius:50%}
.submit{position:absolute;left:244px;top:337px;width:100px;height:20px;border-radius:10px;background:var(--blue);color:var(--white);font-size:12px;line-height:20px;text-align:center}

/* footer */
.footer-col{position:absolute;top:1972px}
.footer-col h4{font-size:10.5px;font-weight:500;color:var(--ink);margin-bottom:13px}
.footer-col p,.footer-col li{font-size:8.5px;line-height:14.3px;color:#555;list-style:none}
.footer-col a{color:var(--blue);text-decoration:none}
.bottom-bar{left:0;top:2141px;width:1200px;height:32px;background:var(--bar);color:#eee;font-size:8px;line-height:32px}
.bottom-bar .copy{position:absolute;left:225px}
.bottom-bar .legal{position:absolute;right:226px}
</style>
</head>
<body>

<header class="site-header">
  <div class="brand" style="left:215px;top:8px;width:130px">
    <span class="brand-mark">Q7M</span>
    <span class="brand-name">QUILL 7 MEADOWS</span>
  </div>
  <nav class="main-nav">
    <a href="#">HOME</a><a href="#">OUR STORY</a><a href="#">TIPS AND TRICKS</a><a href="#">CONTACT US</a><a href="#">FAQ</a>
  </nav>
  <div class="call-pill">
    <span class="call-label">CALL US
      <svg width="17" height="17" viewBox="0 0 17 17"><circle cx="8.5" cy="8.5" r="7.5" fill="none" stroke="#fff" stroke-width="1"/><path d="M7 5l3.5 3.5L7 12" fill="none" stroke="#fff" stroke-width="1.2"/></svg>
    </span>
    <span class="call-number">07 3000 4821</span>
  </div>
</header>

<section>
  <h1 class="abs hero-title">VIRTUAL ASSISTANT?</h1>
  <h2 class="abs hero-sub">MORE LIKE VALUABLE ASSET!</h2>
  <a class="abs btn-quote" href="#">GET A QUOTE</a>
  <div class="abs hero-art" role="img" aria-label="Isometric illustration of a giant clock surrounded by office platforms with small workers at desks and screens"></div>
</section>

<section class="abs intro">
</section>
<h2 class="abs intro-title"><span class="hl">Outsourcing.</span> A big word that means big things <span class="hl">for your business.</span></h2>
<p class="abs intro-copy">Virtual Assistants are the superheroes of the modern office. They can do everything your team can do on a computer at a fraction of the price! (Well, maybe not high five you when you've had a win, but a virtual high five is definitely on the table!)</p>
<div class="abs intro-video" role="img" aria-label="Video still of the two company founders standing in front of a blue wall"></div>

<section class="abs process"></section>
<h2 class="abs process-title">THE PROCCES</h2>
<div class="abs process-line"></div>
<div class="step sm" style="left:225px;top:839px">Step<br>5</div>
<div class="step md" style="left:393px;top:842px">Step<br>1</div>
<div class="step lg" style="left:568px;top:837px">Step<br>2</div>
<div class="step md" style="left:749px;top:842px">Step<br>3</div>
<div class="step sm" style="left:925px;top:839px">Step<br>4</div>

<div class="card far" style="left:226px;top:965px;width:100px;height:76px">
  <h3>Your Magical Journey Begins</h3>
  <p>Now you and your assistant are ready to go. Feel the magic as daily tasks leave your desk and you focus on growth.</p>
</div>
<div class="card near" style="left:325px;top:943px;width:122px;height:119px">
  <h3>Provide Your Preferred Qualities</h3>
  <p>Set up a call with our team to share the skills and duties you need. We then start shortlisting, testing and checking.</p>
</div>
<div class="card near" style="left:763px;top:943px;width:132px;height:119px">
  <h3>The Final Interview</h3>
  <p>The perfect time to get to know them. Ask your questions and pick the chosen one.</p>
</div>
<div class="card far" style="left:893px;top:965px;width:81px;height:76px">
  <h3>Tools</h3>
  <p>Your assistant is ready for work. We set up the tools they need, so you can start.</p>
</div>
<div class="card main" style="left:444px;top:919px;width:322px;height:168px">
  <h3>Endorsing the Shortlisted Candidates</h3>
  <p>After the thorough vetting process, we'll put forward the best candidate. You can then conduct the final interview on your preferred communication platform at a time that suits you. Once the schedule is set, we'll let the candidates know!</p>
</div>

<h2 class="abs services-title">OUR SERVICES</h2>
<p class="abs services-lead">We'll help you save tens (or even hundreds!) of thousands of dollars per year. But what do WE actually do?</p>
<p class="abs services-ask">GLAD YOU ASKED!</p>
<div class="service" style="left:235px">
  <div class="service-ring"><div class="service-art" role="img" aria-label="Illustration of a recruiter reviewing candidate profile cards"></div></div>
  <p>We recruit Virtual Assistants<br>(a.k.a office legends!)<br>, andprovide the tech support<br>for these superheroes!</p>
</div>
<div class="service" style="left:480px">
  <div class="service-ring"><div class="service-art" role="img" aria-label="Illustration of a mobile phone being set up with a wrench and gear"></div></div>
  <p>Set up the phone system<br>(their own Bat Phone!)</p>
</div>
<div class="service" style="left:726px">
  <div class="service-ring"><div class="service-art" role="img" aria-label="Illustration of an award rosette with a star"></div></div>
  <p>We manage Virtual Assistants and keep<br>them in tip-top shape!</p>
</div>

<section class="abs quote"></section>
<h2 class="abs quote-title">GET A QUOTE</h2>
<p class="abs quote-lead">Fill in the form below to get a Quote for your own personal Virtual Assistant</p>
<ul class="abs perks">
  <li><svg width="22" height="22" viewBox="0 0 22 22"><circle cx="11" cy="11" r="10" fill="#fff" stroke="#333" stroke-width="1.2"/><circle cx="11" cy="11" r="7" fill="none" stroke="#333" stroke-width="1"/><path d="M7 11l3 3 5-6" fill="none" stroke="#333" stroke-width="1.6"/></svg>Your Own Virtual Assistant</li>
  <li><svg width="22" height="22" viewBox="0 0 22 22"><circle cx="11" cy="11" r="10" fill="#fff" stroke="#333" stroke-width="1.2"/><circle cx="11" cy="11" r="7" fill="none" stroke="#333" stroke-width="1"/><path d="M7 11l3 3 5-6" fill="none" stroke="#333" stroke-width="1.6"/></svg>One Invoice Per Month</li>
  <li><svg width="22" height="22" viewBox="0 0 22 22"><circle cx="11" cy="11" r="10" fill="#fff" stroke="#333" stroke-width="1.2"/><circle cx="11" cy="11" r="7" fill="none" stroke="#333" stroke-width="1"/><path d="M7 11l3 3 5-6" fill="none" stroke="#333" stroke-width="1.6"/></svg>No Super or TAX</li>
  <li><svg width="22" height="22" viewBox="0 0 22 22"><circle cx="11" cy="11" r="10" fill="#fff" stroke="#333" stroke-width="1.2"/><circle cx="11" cy="11" r="7" fill="none" stroke="#333" stroke-width="1"/><path d="M7 11l3 3 5-6" fill="none" stroke="#333" stroke-width="1.6"/></svg>Dedicated To Your Business Only</li>
  <li><svg width="22" height="22" viewBox="0 0 22 22"><circle cx="11" cy="11" r="10" fill="#fff" stroke="#333" stroke-width="1.2"/><circle cx="11" cy="11" r="7" fill="none" stroke="#333" stroke-width="1"/><path d="M7 11l3 3 5-6" fill="none" stroke="#333" stroke-width="1.6"/></svg>Dedicated Phone System</li>
  <li><svg width="22" height="22" viewBox="0 0 22 22"><circle cx="11" cy="11" r="10" fill="#fff" stroke="#333" stroke-width="1.2"/><circle cx="11" cy="11" r="7" fill="none" stroke="#333" stroke-width="1"/><path d="M7 11l3 3 5-6" fill="none" stroke="#333" stroke-width="1.6"/></svg>IT Setup and Support</li>
</ul>

<form class="abs quote-form">
  <div class="field" style="top:19px"><span class="field-label">Bussniess Name<svg width="17" height="17" viewBox="0 0 17 17"><circle cx="8.5" cy="8.5" r="7.5" fill="none" stroke="#fff"/><path d="M7 5l3.5 3.5L7 12" fill="none" stroke="#fff" stroke-width="1.2"/></svg></span></div>
  <div class="field" style="top:59px"><span class="field-label">First Name<svg width="17" height="17" viewBox="0 0 17 17"><circle cx="8.5" cy="8.5" r="7.5" fill="none" stroke="#fff"/><path d="M7 5l3.5 3.5L7 12" fill="none" stroke="#fff" stroke-width="1.2"/></svg></span></div>
  <div class="field" style="top:99px"><span class="field-label">Surname<svg width="17" height="17" viewBox="0 0 17 17"><circle cx="8.5" cy="8.5" r="7.5" fill="none" stroke="#fff"/><path d="M7 5l3.5 3.5L7 12" fill="none" stroke="#fff" stroke-width="1.2"/></svg></span></div>
  <div class="field" style="top:139px"><span class="field-label">Contact Number<svg width="17" height="17" viewBox="0 0 17 17"><circle cx="8.5" cy="8.5" r="7.5" fill="none" stroke="#fff"/><path d="M7 5l3.5 3.5L7 12" fill="none" stroke="#fff" stroke-width="1.2"/></svg></span></div>
  <div class="field" style="top:179px"><span class="field-label">Email<svg width="17" height="17" viewBox="0 0 17 17"><circle cx="8.5" cy="8.5" r="7.5" fill="none" stroke="#fff"/><path d="M7 5l3.5 3.5L7 12" fill="none" stroke="#fff" stroke-width="1.2"/></svg></span></div>
  <div class="field-area"><div class="field-label">Describe the tasks you'll need from your<br>Virtual Assistant<svg width="26" height="26" viewBox="0 0 26 26"><circle cx="13" cy="13" r="12" fill="none" stroke="#fff"/><path d="M7 11l6 6 6-6" fill="none" stroke="#fff" stroke-width="1.3"/></svg></div></div>
  <span class="subscribe">Subscribe to our newsletter</span>
  <span class="submit">Submit</span>
</form>

<div class="footer-col" style="left:225px;width:200px">
  <h4>ABOUT US</h4>
  <p>Lorem ipsum dolor sit amet, consectetur adipiscing elit, sed do eiusmod tempor incididunt ut labore et dolore magna aliqua. Quis ipsum suspendisse ultrices gravida. Risus commodo viverra maecenas accumsan lacus vel facilisis.</p>
</div>
<div class="footer-col" style="left:537px">
  <h4>QUICK LINKS</h4>
  <ul><li>HOME</li><li>OUR STORY</li><li>TIPS AND TRICKS</li><li>CONTACT US</li><li>FAQ</li></ul>
</div>
<div class="brand" style="left:507px;top:2090px;width:130px">
  <span class="brand-mark">Q7M</span>
  <span class="brand-name">QUILL 7 MEADOWS</span>
</div>
<div class="footer-col" style="left:847px">
  <h4>CONTACT</h4>
  <p>Dara Penwick<br>Mobile: 0400 512 078<br>Email:<br><a href="#">dara@quill7meadows.com.au</a></p>
  <p style="margin-top:14px">Milo Trevane<br>Mobile: 0400 386 914<br>Email:<br><a href="#">milo@quill7meadows.com.au</a></p>
</div>

<footer class="abs bottom-bar">
  <span class="copy">© 2019 QUILL 7 MEADOWS | ALL RIGHTS RESERVED.</span>
  <span class="legal">Terms of Service / Privacy Policy / Contact Us</span>
</footer>

</body>
</html>
```